School Signage

I am wanting designs for signs completed that prompt students of the school requirements for hats, preparation and play.

I've uploaded rough examples of what we're after, but we would like them stylised and better than the example, including:
- A stylised logo/graphic for the 'Mervale 1, 2, 3'
- Clear, crisp signage for the words.
- Graphics that reinforce the message of the sign.

We're after three signs:
- One that will be located on the oval to prompt hat use.
- One that will be near the entry prompting the morning routine (please make this one landscape with instructions for 'on time' on one side, and 'late' on the other).
- One that will be located within the school prompting readiness for class.

```html
<!DOCTYPE html>
<html lang="en">
<head>
<meta charset="utf-8">
<title>Ready for Class – Mervale 1, 2, 3</title>
<link rel="stylesheet" href="https://fonts.googleapis.com/css2?family=Anton&family=Archivo:wght@800&family=Montserrat:wght@800&display=swap">
<style>
  :root {
    --sign-yellow: #ffe500;
    --school-green: #003b0d;
    --accent-green: #0a4a14;
    --pattern-green: #11501c;
    --ink: #141414;
    --white: #ffffff;
  }
  * { margin: 0; padding: 0; box-sizing: border-box; }
  html, body { width: 872px; height: 1200px; overflow: hidden; background: #666; }
  .sign {
    position: relative;
    width: 872px;
    height: 1200px;
    background: var(--sign-yellow);
    overflow: hidden;
    font-family: "Archivo", Arial, sans-serif;
    color: var(--ink);
  }
  .headline {
    position: absolute;
    top: 78px;
    left: 0;
    width: 100%;
    text-align: center;
    font-family: "Anton", "Impact", sans-serif;
    font-size: 108px;
    line-height: 96px;
    letter-spacing: 1px;
    color: var(--ink);
    padding-left: 20px;
  }
  .program-pill {
    position: absolute;
    left: 168px;
    top: 286px;
    width: 519px;
    height: 73px;
    border-radius: 37px;
    background: var(--school-green);
    color: var(--white);
    font-family: "Montserrat", Arial, sans-serif;
    font-size: 38px;
    line-height: 73px;
    text-align: center;
    padding-right: 30px;
  }
  .checklist { position: absolute; left: 79px; top: 396px; width: 711px; list-style: none; }
  .checklist-item {
    position: relative;
    display: flex;
    align-items: center;
    height: 118px;
    border-bottom: 1.5px solid var(--ink);
  }
  .checklist-item:nth-child(2) { height: 131px; }
  .checklist-item:last-child { border-bottom: none; height: 140px; align-items: flex-start; padding-top: 20px; }
  .item-icon { width: 94px; height: 94px; margin-left: 13px; flex: none; }
  .checklist-item:last-child .item-icon { margin-top: 4px; }
  .item-number {
    width: 68px;
    margin-left: 30px;
    font-size: 52px;
    color: var(--accent-green);
    flex: none;
  }
  .item-text { font-size: 52px; line-height: 60px; letter-spacing: 0.5px; }
  .footer-band { position: absolute; left: 0; top: 830px; width: 872px; height: 370px; }
  .footer-pattern { position: absolute; left: 0; bottom: 0; width: 872px; height: 110px;
    background: linear-gradient(180deg, var(--school-green) 0%, var(--pattern-green) 100%); }
  .school-mark {
    position: absolute;
    left: 92px;
    top: 880px;
    width: 220px;
    display: flex;
    flex-direction: column;
    align-items: center;
    gap: 14px;
  }
  .school-mark-dot { width: 110px; height: 110px; border-radius: 50%; background: var(--sign-yellow); }
  .school-mark-name {
    font-family: "Montserrat", Arial, sans-serif;
    font-size: 30px;
    color: var(--sign-yellow);
    letter-spacing: 1px;
  }
  .values { position: absolute; right: 84px; top: 984px; text-align: right; }
  .values-title {
    font-family: "Anton", "Impact", sans-serif;
    font-size: 50px;
    line-height: 54px;
    color: var(--sign-yellow);
    letter-spacing: 0.5px;
  }
  .values-sub {
    margin-top: 6px;
    font-family: "Montserrat", Arial, sans-serif;
    font-size: 27px;
    color: var(--white);
    letter-spacing: 0.5px;
  }
</style>
</head>
<body>
<main class="sign">
  <h1 class="headline">ARE YOU READY<br>FOR CLASS?</h1>
  <div class="program-pill">THE MERVALE 1, 2, 3</div>

  <ol class="checklist">
    <li class="checklist-item">
      <svg class="item-icon" viewBox="0 0 94 94" aria-hidden="true">
        <circle cx="47" cy="47" r="47" fill="#141414"/>
        <rect x="27" y="26" width="40" height="28" rx="3" fill="#fff"/>
        <path d="M20 58 H74 L69 68 H25 Z" fill="#fff"/>
        <rect x="41" y="60" width="12" height="3" rx="1.5" fill="#141414"/>
      </svg>
      <span class="item-number">1.</span>
      <span class="item-text">Laptop/workbook</span>
    </li>
    <li class="checklist-item">
      <svg class="item-icon" viewBox="0 0 94 94" aria-hidden="true">
        <circle cx="47" cy="47" r="47" fill="#141414"/>
        <rect x="32" y="17" width="30" height="60" rx="5" fill="#fff"/>
        <rect x="42" y="21" width="10" height="2.5" rx="1.2" fill="#141414"/>
        <circle cx="47" cy="70" r="3" fill="#141414"/>
      </svg>
      <span class="item-number">2.</span>
      <span class="item-text">Phone in Lockpouch</span>
    </li>
    <li class="checklist-item">
      <svg class="item-icon" viewBox="0 0 94 94" aria-hidden="true">
        <circle cx="47" cy="47" r="47" fill="#141414"/>
        <path d="M30 58 C28 38 40 24 54 24 C68 24 76 38 74 58 Z" fill="#fff"/>
        <path d="M30 58 C24 60 16 66 14 72 C28 70 44 66 60 60 Z" fill="#fff"/>
        <path d="M52 25 C46 34 44 46 46 58" stroke="#141414" stroke-width="2" fill="none"/>
        <circle cx="54" cy="24" r="3" fill="#141414"/>
      </svg>
      <span class="item-number">3.</span>
      <span class="item-text">Correct uniform<br>(including hat)</span>
    </li>
  </ol>

  <svg class="footer-band" viewBox="0 0 872 370" preserveAspectRatio="none" aria-hidden="true">
    <path d="M0 14 C40 24 70 50 110 72 L240 90 C300 110 380 108 470 62 C560 18 640 40 700 70 C760 100 820 76 872 64 V370 H0 Z" fill="#141414"/>
    <path d="M0 26 C40 36 70 62 110 84 L240 102 C300 122 380 120 470 76 C560 34 640 52 700 82 C760 112 820 88 872 74 V370 H0 Z" fill="var(--school-green)"/>
  </svg>
  <div class="footer-pattern" role="img" aria-label="Subtle dotted wave pattern along the bottom edge"></div>

  <div class="school-mark">
    <span class="school-mark-dot"></span>
    <span class="school-mark-name">MERVALE</span>
  </div>

  <div class="values">
    <p class="values-title">CURIOSITY AND DRIVE</p>
    <p class="values-sub">MERVALE LEARNER VALUES</p>
  </div>
</main>
</body>
</html>
```